Web Dashboard for manufacturing data

We need a dashboard for website to show statistical information on buttons/cards/tiles. There will be 12 buttons on the screen (laptop, tablet) On these buttons there are several key pieces of information on each button. 1) Largest info is % 0-100%. 2) 4 status colours neutral, green, yellow, red. 3) Title- up to 20 characters 4) target here is an example... target=above 90%.- When these buttons are tapped, they take user to more info for that specific data.
1 page

```html
<!DOCTYPE html>
<html lang="en">
<head>
<meta charset="utf-8">
<title>Manufacturing Dashboard</title>
<link rel="stylesheet" href="https://fonts.googleapis.com/css2?family=Poppins:wght@400;500;600&family=Inter:wght@600;700&display=swap">
<style>
  :root {
    --brand: #0152a8;
    --page: #cadcee;
    --white: #ffffff;
    --nav-text: #b9d2f2;
    --dial-face: #6e9fd3;
    --dial-ring: #0a4a96;
    --dial-text: #1d2b3d;
    --card-text: #dbe7f7;
    --green: #19e021;
    --yellow: #f2dc14;
    --red: #e5182a;
  }
  * { box-sizing: border-box; margin: 0; padding: 0; }
  html, body { width: 1200px; height: 853px; overflow: hidden; }
  body { background: var(--page); font-family: "Poppins", sans-serif; position: relative; }

  .sidebar { position: absolute; left: 0; top: 0; width: 288px; height: 853px; background: var(--brand); }
  .brand { position: absolute; left: 38px; top: 44px; display: flex; align-items: center; gap: 13px; }
  .brand-square { width: 40px; height: 40px; border-radius: 9px; background: #cfe0f5; }
  .brand-name { color: var(--white); font-size: 30px; font-weight: 600; letter-spacing: -0.5px; }

  .nav { list-style: none; }
  .nav-item { position: absolute; left: 0; width: 288px; height: 53px; display: flex; align-items: center; color: var(--nav-text); font-size: 15px; font-weight: 500; }
  .nav-item svg { position: absolute; left: 57px; width: 32px; height: 32px; fill: none; stroke: currentColor; stroke-width: 2; stroke-linecap: round; stroke-linejoin: round; }
  .nav-item span { position: absolute; left: 112px; }
  .nav-item.active { left: 38px; width: 250px; background: var(--white); border-radius: 27px 0 0 27px; color: var(--brand); }
  .nav-item.active svg { left: 19px; }
  .nav-item.active span { left: 74px; }

  .tile { position: absolute; width: 130px; height: 176px; background: var(--brand); border-radius: 3px; box-shadow: 4px 5px 6px rgba(0,0,0,0.35); text-align: center; }
  .dial { position: absolute; left: 0; top: 0; width: 130px; height: 100px; }
  .dial-value { font-family: "Inter", sans-serif; font-size: 14px; font-weight: 700; fill: var(--dial-text); }
  .tile-title { position: absolute; left: 0; right: 0; top: 97px; color: var(--card-text); font-family: "Inter", sans-serif; font-weight: 700; font-size: 13px; line-height: 15px; }
  .tile-target { position: absolute; left: 0; right: 0; top: 140px; color: var(--card-text); font-family: "Inter", sans-serif; font-weight: 600; font-size: 7.5px; line-height: 11.5px; }

  .c1 { left: 352px; } .c2 { left: 540px; } .c3 { left: 727px; } .c4 { left: 915px; }
  .r1 { top: 111px; } .r2 { top: 329px; } .r3 { top: 547px; }
</style>
</head>
<body>
<svg width="0" height="0" style="position:absolute">
  <defs>
    <symbol id="dial-base" viewBox="0 0 130 100">
      <circle cx="64" cy="49" r="38" fill="var(--dial-ring)"/>
      <circle cx="64" cy="49" r="31" fill="var(--dial-face)" stroke="#8db6e2" stroke-width="1.5"/>
    </symbol>
  </defs>
</svg>

<aside class="sidebar">
  <div class="brand"><div class="brand-square"></div><div class="brand-name">Logo</div></div>
  <ul class="nav">
    <li class="nav-item active" style="top:125px">
      <svg viewBox="0 0 32 32"><path d="M5 14 16 4l11 10v13H5z"/><path d="M13 27v-8h6v8"/></svg><span>Dashboard</span>
    </li>
    <li class="nav-item" style="top:189px">
      <svg viewBox="0 0 32 32"><rect x="5" y="7" width="22" height="20" rx="2"/><path d="M5 13h22M11 4v6M21 4v6M15 4v6"/></svg><span>Event</span>
    </li>
    <li class="nav-item" style="top:255px">
      <svg viewBox="0 0 32 32"><circle cx="20" cy="9" r="6"/><path d="M20 6v6M18 8h3M2 21l6-4h6l2 2h-6M10 21h8l9-5-2 6-9 5H8l-5 2"/></svg><span>Finance</span>
    </li>
    <li class="nav-item" style="top:322px">
      <svg viewBox="0 0 32 32"><circle cx="16" cy="10" r="6"/><path d="M6 28v-4a5 5 0 0 1 5-5h10a5 5 0 0 1 5 5v4z"/></svg><span>User</span>
    </li>
    <li class="nav-item" style="top:388px">
      <svg viewBox="0 0 32 32"><path d="M12 5h16v12h-4v4l-4-4h-8z"/><path d="M12 11H4v12h4v4l4-4h8v-6"/></svg><span>Chat</span>
    </li>
    <li class="nav-item" style="top:455px">
      <svg viewBox="0 0 32 32"><path d="M2 17h6l4-9 6 18 4-9h8"/></svg><span>Lastest Activity</span>
    </li>
  </ul>
</aside>

<main class="tiles">
  <!-- Row 1 -->
  <a class="tile c1 r1"><svg class="dial" viewBox="0 0 130 100"><use href="#dial-base"/><path d="M32.8 67 A36 36 0 0 1 91.6 25.9" fill="none" stroke="var(--green)" stroke-width="4" stroke-linecap="round"/><text class="dial-value" x="64" y="54" text-anchor="middle">91%</text></svg><div class="tile-title">Example<br>TitleUpTo 20</div><div class="tile-target">Target:<br>above 90%</div></a>
  <a class="tile c2 r1"><svg class="dial" viewBox="0 0 130 100"><use href="#dial-base"/><path d="M32.8 67 A36 36 0 0 1 91.6 25.9" fill="none" stroke="var(--yellow)" stroke-width="4" stroke-linecap="round"/><text class="dial-value" x="64" y="54" text-anchor="middle">85%</text></svg><div class="tile-title">Example<br>TitleUpTo 20</div><div class="tile-target">Target:<br>above 90%</div></a>
  <a class="tile c3 r1"><svg class="dial" viewBox="0 0 130 100"><use href="#dial-base"/><path d="M32.8 67 A36 36 0 0 1 91.6 25.9" fill="none" stroke="var(--red)" stroke-width="4" stroke-linecap="round"/><text class="dial-value" x="64" y="54" text-anchor="middle">51%</text></svg><div class="tile-title">Example<br>TitleUpTo 20</div><div class="tile-target">Target:<br>above 90%</div></a>
  <a class="tile c4 r1"><svg class="dial" viewBox="0 0 130 100"><use href="#dial-base"/><path d="M32.8 67 A36 36 0 0 1 91.6 25.9" fill="none" stroke="var(--green)" stroke-width="4" stroke-linecap="round"/><text class="dial-value" x="64" y="54" text-anchor="middle">91%</text></svg><div class="tile-title">Example<br>TitleUpTo 20</div><div class="tile-target">Target:<br>above 90%</div></a>
  <!-- Row 2 -->
  <a class="tile c1 r2"><svg class="dial" viewBox="0 0 130 100"><use href="#dial-base"/><path d="M32.8 67 A36 36 0 0 1 91.6 25.9" fill="none" stroke="var(--green)" stroke-width="4" stroke-linecap="round"/><text class="dial-value" x="64" y="54" text-anchor="middle">91%</text></svg><div class="tile-title">Example<br>TitleUpTo 20</div><div class="tile-target">Target:<br>above 90%</div></a>
  <a class="tile c2 r2"><svg class="dial" viewBox="0 0 130 100"><use href="#dial-base"/><path d="M32.8 67 A36 36 0 0 1 91.6 25.9" fill="none" stroke="var(--green)" stroke-width="4" stroke-linecap="round"/><text class="dial-value" x="64" y="54" text-anchor="middle">91%</text></svg><div class="tile-title">Example<br>TitleUpTo 20</div><div class="tile-target">Target:<br>above 90%</div></a>
  <a class="tile c3 r2"><svg class="dial" viewBox="0 0 130 100"><use href="#dial-base"/><path d="M32.8 67 A36 36 0 0 1 91.6 25.9" fill="none" stroke="var(--green)" stroke-width="4" stroke-linecap="round"/><text class="dial-value" x="64" y="54" text-anchor="middle">91%</text></svg><div class="tile-title">Example<br>TitleUpTo 20</div><div class="tile-target">Target:<br>above 90%</div></a>
  <a class="tile c4 r2"><svg class="dial" viewBox="0 0 130 100"><use href="#dial-base"/><path d="M32.8 67 A36 36 0 0 1 91.6 25.9" fill="none" stroke="var(--green)" stroke-width="4" stroke-linecap="round"/><text class="dial-value" x="64" y="54" text-anchor="middle">91%</text></svg><div class="tile-title">Example<br>TitleUpTo 20</div><div class="tile-target">Target:<br>above 90%</div></a>
  <!-- Row 3 -->
  <a class="tile c1 r3"><svg class="dial" viewBox="0 0 130 100"><use href="#dial-base"/><path d="M32.8 67 A36 36 0 0 1 91.6 25.9" fill="none" stroke="var(--green)" stroke-width="4" stroke-linecap="round"/><text class="dial-value" x="64" y="54" text-anchor="middle">91%</text></svg><div class="tile-title">Example<br>TitleUpTo 20</div><div class="tile-target">Target:<br>above 90%</div></a>
  <a class="tile c2 r3"><svg class="dial" viewBox="0 0 130 100"><use href="#dial-base"/><path d="M32.8 67 A36 36 0 0 1 91.6 25.9" fill="none" stroke="var(--green)" stroke-width="4" stroke-linecap="round"/><text class="dial-value" x="64" y="54" text-anchor="middle">91%</text></svg><div class="tile-title">Example<br>TitleUpTo 20</div><div class="tile-target">Target:<br>above 90%</div></a>
  <a class="tile c3 r3"><svg class="dial" viewBox="0 0 130 100"><use href="#dial-base"/><path d="M32.8 67 A36 36 0 0 1 91.6 25.9" fill="none" stroke="var(--green)" stroke-width="4" stroke-linecap="round"/><text class="dial-value" x="64" y="54" text-anchor="middle">91%</text></svg><div class="tile-title">Example<br>TitleUpTo 20</div><div class="tile-target">Target:<br>above 90%</div></a>
  <a class="tile c4 r3"><svg class="dial" viewBox="0 0 130 100"><use href="#dial-base"/><path d="M32.8 67 A36 36 0 0 1 91.6 25.9" fill="none" stroke="var(--green)" stroke-width="4" stroke-linecap="round"/><text class="dial-value" x="64" y="54" text-anchor="middle">91%</text></svg><div class="tile-title">Example<br>TitleUpTo 20</div><div class="tile-target">Target:<br>above 90%</div></a>
</main>
</body>
</html>
```